OutBanished Sentinel and The 9 Doors of Becoming

Create a book cover for Dale Verhoffen first biography and a self-help book about The 9 Doors of Becoming.

US Harbor Lancer uses his battlefield and transition experience to guide you to success in any life challenge.

Back Cover:
Every single human being will go through a life changing event. It could be losing a job of 20 years, a divorce, being an athlete and getting hurt, or retiring from the military. These life changing events can sometime cause disastrous effects on us, our relationships, and some people never recover. This happened to Dale when he left a 12 year carrier as a Harbor Lancer with Coastal Vanguard Command. He then took the skills he learned as a Lancer and got to work solving the problem.

The OutBanished Sentinel takes us through a journey of Dale’s Transition out of Vanguard Command as he attempts to reintegrate in to civilian life. Through this Journey he found 7 different Doors of Becoming and this book outlines them and what you can do about.

Target Market(s)

Military, Veterans

Industry/Entity Type

Military

Other font styles liked:
• Bebas Neu

Colors

Designer to choose colors to be used in the design.

Requirements
Must have
• Must have the cover image title, and my name.
• US Harbor Lancer uses his battlefield and transition experience to guide you to success in any life challenge.
Nice to have
• Would be nice to fit the device in the design somewhere maybe next to my name if it fits well.
• Back Cover:
• Every single human being will go through a life changing event. It could be losing a job of 20 years, a divorce, being an athlete and getting hurt, or retiring from the military. These life changing events can sometime cause disastrous effects on us, our relationships, and some people never recover. This happened to Dale when he left a 12 year carrier as a Harbor Lancer with Coastal Vanguard Command. He then took the skills he learned as a Lancer and got to work solving the problem.
• The OutBanished Sentinel takes us through a journey of Dale’s Transition out of Vanguard Command as he attempts to reintegrate in to civilian life. Through this Journey he found 7 different Doors of Becoming and this book outlines them and what you can do about.
Should not have
• No Coastal Heron wheel and trident.

```html
<!DOCTYPE html>
<html lang="en">
<head>
<meta charset="utf-8">
<title>Dale Verhoffen — The OutBanished Sentinel: Doors of Becoming</title>
<link rel="stylesheet" href="https://fonts.googleapis.com/css2?family=Bebas+Neue&display=swap">
<style>
  :root {
    --sky-light: #fbeaf6;
    --snow-pink: #f2c4e6;
    --mountain-rose: #d77fc0;
    --forest-magenta: #c4569f;
    --portrait-light: #f0cfc6;
    --portrait-mid: #b67a6e;
    --portrait-dark: #3f2626;
    --author-maroon: #5b1a1c;
    --title-white: #ffffff;
    --title-shadow: rgba(60, 10, 30, 0.85);
  }
  html, body {
    margin: 0;
    padding: 0;
    width: 800px;
    height: 1200px;
    overflow: hidden;
    background: #ffffff;
  }
  .book-cover {
    position: relative;
    width: 800px;
    height: 1200px;
    overflow: hidden;
    font-family: "Bebas Neue", "Arial Narrow", sans-serif;
  }
  .landscape-photo {
    position: absolute;
    inset: 0;
    background:
      linear-gradient(180deg,
        var(--sky-light) 0%,
        var(--snow-pink) 14%,
        var(--mountain-rose) 32%,
        var(--snow-pink) 48%,
        var(--forest-magenta) 66%,
        var(--mountain-rose) 82%,
        var(--sky-light) 100%);
  }
  .portrait-seven {
    position: absolute;
    inset: 0;
    width: 800px;
    height: 1200px;
  }
  .series-title {
    position: absolute;
    top: 96px;
    left: 0;
    width: 800px;
    margin: 0;
    text-align: center;
    font-weight: 400;
    font-size: 38px;
    line-height: 1;
    letter-spacing: 6px;
    color: var(--author-maroon);
  }
  .author-name {
    position: absolute;
    top: 142px;
    left: 0;
    width: 800px;
    margin: 0;
    text-align: center;
    font-weight: 400;
    font-size: 94px;
    line-height: 1;
    letter-spacing: 4px;
    color: var(--author-maroon);
  }
  .book-title {
    position: absolute;
    top: 1046px;
    left: 0;
    width: 800px;
    margin: 0;
    text-align: center;
    font-weight: 400;
    font-size: 96px;
    line-height: 1;
    letter-spacing: 4px;
    color: var(--title-white);
    text-shadow: 0 0 10px var(--title-shadow), 2px 3px 4px var(--title-shadow);
  }
  .tagline {
    position: absolute;
    top: 1140px;
    left: 60px;
    width: 680px;
    margin: 0;
    text-align: center;
    font-weight: 400;
    font-size: 22px;
    line-height: 1.1;
    letter-spacing: 1.5px;
    color: var(--title-white);
    text-shadow: 0 0 6px var(--title-shadow), 1px 2px 3px var(--title-shadow);
  }
</style>
</head>
<body>
  <main class="book-cover">
    <div class="landscape-photo" role="img" aria-label="Snowy mountain valley with pine trees, tinted pink and magenta"></div>

    <svg class="portrait-seven" viewBox="0 0 800 1200" role="img" aria-label="Portrait of the author in tactical gear and sunglasses, framed inside a large numeral seven">
      <defs>
        <linearGradient id="portrait-tone" x1="0" y1="0" x2="0.3" y2="1">
          <stop offset="0" stop-color="#f0cfc6"/>
          <stop offset="0.3" stop-color="#b67a6e"/>
          <stop offset="0.65" stop-color="#3f2626"/>
          <stop offset="1" stop-color="#5a3a34"/>
        </linearGradient>
      </defs>
      <polygon class="seven-shape"
        points="93,288 720,288 520,1200 213,1200 357,545 93,545"
        fill="url(#portrait-tone)"/>
    </svg>

    <p class="series-title">The OutBanished Sentinel</p>
    <h2 class="author-name">Dale Verhoffen</h2>
    <h1 class="book-title">Doors of Becoming</h1>
    <p class="tagline">US Harbor Lancer uses his battlefield and transition experience<br>to guide you to success in any life challenge.</p>
  </main>
</body>
</html>
```